Lorna and Vikram Destination Wedding Invitation

THE DESIGN
- We need a unique, fun and colourful wedding invitation.
- We would like the designs to be printed using letterpress (not block) and or laser cut. Open to suggestions.
- We would like to include the attached wedding logo.
- We would like a design that is fun yet classy.
- 3D if possible.
- Main colour: deep purple; secondary colour: green.

Colour example:
http://www.bloomvowshop.com/Soft-Petal-Marigold-Sprays-Posyp/mkrtz412.htm
- we did think about using the following product to enclose the necessary cards. This is not mandatory. http://www.vowsandtiesstore.co.uk/product/willow-fold-invitation#colour=19

TO AVOID
- Paisleys
- Obvious flowers
- Block letterpress

FAVOURED DESIGNS
http://i0.wp.com/www.inkmorrow.com/images/blog-images/cedar-lantern1.jpg?resize=400%2C533
http://studioferlune.com/collection-corvane.html
http://studioferlune.com/collection-baldric.html
https://www.craftlymart.com/listing/847362915/fougere-wedding-invitation-laser-cut

THE COUPLE
- Bride: Lorna Maeve Castellanos
- Groom: Vikram Dalbeth
- Both from Sydney, Australia
- Both living in London, UK
- Website: lornaandvikram.com

THE WEDDING:
- We are getting married in Koh Samui, Thailand, early next year.
- We have 3 official events, the welcome drinks (March 25), the wedding (March 27) and beach bbq (March 28).

THE INVITE -1 CARD design
For everyone, a page/card that will include the following:
- Reception/ Main invite
- Location card (Direction/Map). Venue: Tharuvan Cove Spa Resort
- RSVP - via website
See wording attachment for details.

I need an insert (template) for the following: - 1 design only.
- Tide Lantern Night
- Tots Hollow (for people with children)
- Rehearsal

ADDITIONAL
- We would like the design to be adaptable for place cards and or wedding programs (normal printer).

Please let me know if you need more information.

Target Market(s)

Fun, casual, unique

Industry/Entity Type

Wedding

Colors
6b449b
876aae
b7a5cd

Requirements
Must have
• Wedding logo
Nice to have
• Please see project description
Should not have

```html
<!DOCTYPE html>
<html lang="en">
<head>
<meta charset="utf-8">
<title>Maeve Castellanos &amp; Vikram Dalbeth — Wedding Invitation</title>
<link href="https://fonts.googleapis.com/css2?family=Dancing+Script:wght@500;700&display=swap" rel="stylesheet">
<style>
  :root {
    --plum-deep: #3f0b4d;
    --plum: #4e1260;
    --plum-glow: #5c1b6f;
    --leaf: #3fc24a;
    --leaf-dark: #1f8a2e;
    --ink: #ffffff;
    --mark: #c9a8e0;
  }
  html, body {
    margin: 0;
    padding: 0;
    overflow: hidden;
    background: #ffffff;
  }
  .invitation {
    position: relative;
    width: 833px;
    height: 1200px;
    overflow: hidden;
    background: radial-gradient(ellipse at 50% 45%, var(--plum-glow) 0%, var(--plum) 55%, var(--plum-deep) 100%);
    font-family: "Dancing Script", cursive;
    color: var(--ink);
  }
  .ornament {
    position: absolute;
    left: 0;
    width: 833px;
  }
  .ornament--top {
    top: 0;
    height: 165px;
  }
  .ornament--bottom {
    bottom: 0;
    height: 190px;
  }
  .wedding-mark {
    position: absolute;
    top: 215px;
    left: 0;
    width: 833px;
    display: flex;
    justify-content: center;
    align-items: center;
    gap: 10px;
    font-size: 28px;
    font-weight: 500;
    color: var(--mark);
  }
  .wedding-mark__dot {
    width: 12px;
    height: 12px;
    border-radius: 50%;
    background: var(--mark);
  }
  .name {
    position: absolute;
    text-align: center;
    line-height: 1;
    font-weight: 700;
  }
  .name__first {
    display: block;
    font-size: 104px;
  }
  .name__last {
    display: block;
    font-size: 50px;
    font-weight: 500;
    margin-top: 4px;
  }
  .name--bride {
    left: 40px;
    top: 380px;
    width: 340px;
  }
  .name--groom {
    left: 450px;
    top: 380px;
    width: 340px;
  }
  .ampersand {
    position: absolute;
    left: 392px;
    top: 445px;
    width: 50px;
    text-align: center;
    font-size: 54px;
    font-weight: 500;
  }
  .date {
    position: absolute;
    left: 0;
    top: 575px;
    width: 833px;
    text-align: center;
    line-height: 1;
  }
  .date__month {
    display: block;
    font-size: 46px;
    font-weight: 500;
  }
  .date__day {
    display: block;
    font-size: 104px;
    font-weight: 700;
    margin-top: -4px;
  }
  .date__year {
    position: absolute;
    left: 360px;
    top: 148px;
    font-size: 28px;
    font-weight: 500;
  }
  .rsvp {
    position: absolute;
    left: 0;
    top: 952px;
    width: 833px;
    text-align: center;
    font-size: 18px;
    font-weight: 500;
  }
</style>
</head>
<body>
<main class="invitation">
  <svg class="ornament ornament--top" viewBox="0 0 833 165" role="img" aria-label="Green laser-cut filigree border along the top edge">
    <defs>
      <linearGradient id="leafTop" x1="0" y1="0" x2="0" y2="1">
        <stop offset="0" stop-color="var(--leaf-dark)"/>
        <stop offset="1" stop-color="var(--leaf)"/>
      </linearGradient>
    </defs>
    <path d="M0 0 H833 V70 C760 110 690 60 620 100 C560 135 500 110 460 150 C440 165 393 165 373 150 C333 110 273 135 213 100 C143 60 73 110 0 70 Z" fill="url(#leafTop)"/>
  </svg>

  <div class="wedding-mark">
    <span class="wedding-mark__dot"></span>
    <span>Lorna &amp; Vikram</span>
  </div>

  <h1 class="name name--bride">
    <span class="name__first">Maeve</span>
    <span class="name__last">Castellanos</span>
  </h1>
  <div class="ampersand">&amp;</div>
  <h1 class="name name--groom">
    <span class="name__first">Vikram</span>
    <span class="name__last">Dalbeth</span>
  </h1>

  <div class="date">
    <span class="date__month">march</span>
    <span class="date__day">27</span>
    <span class="date__year">2016</span>
  </div>

  <p class="rsvp">Rsvp: www.lornaandvikram.com</p>

  <svg class="ornament ornament--bottom" viewBox="0 0 833 190" role="img" aria-label="Green laser-cut filigree border along the bottom edge">
    <defs>
      <linearGradient id="leafBottom" x1="0" y1="1" x2="0" y2="0">
        <stop offset="0" stop-color="var(--leaf-dark)"/>
        <stop offset="1" stop-color="var(--leaf)"/>
      </linearGradient>
    </defs>
    <path d="M0 190 H833 V90 C770 70 700 110 640 80 C580 50 520 70 480 30 C455 5 378 5 353 30 C313 70 253 50 193 80 C133 110 63 70 0 90 Z" fill="url(#leafBottom)"/>
  </svg>
</main>
</body>
</html>
```